BOLD & MINIMALIST DESIGN NEEDED

We want a very bold but minimalistic business card design that is impactful and utilizes both sides of the business card. Our current logo is included for your use.

We want bold fonts and good use of negative space. We don't want the logo to overpower the design.

Target Market(s)

Professionals who are building new commercial buildings.

Industry/Entity Type

Construction

Contact Information for Business Card

Name, Title, email, office phone, cell phone, website

Font styles to use
Serif
Sans Serif

Requirements
Must have
• Bold design!

```html
<!DOCTYPE html>
<html lang="en">
<head>
<meta charset="utf-8">
<title>Summitline Design + Build – Business Card</title>
<link rel="stylesheet" href="https://fonts.googleapis.com/css2?family=Roboto:wght@400;700&family=Roboto+Condensed:wght@700&display=swap">
<style>
  :root {
    --page-bg: #d9d4cc;
    --panel-dark: #1e1f20;
    --panel-dark-edge: #2b2c2d;
    --frost-light: #eef0f1;
    --frost-mid: #d7dadc;
    --accent-green: #4f9a2c;
    --text-light: #e6e6e6;
    --text-muted: #cfcfcf;
    --brand-ink: #161616;
  }
  * { box-sizing: border-box; margin: 0; padding: 0; }
  html, body { width: 1200px; height: 970px; overflow: hidden; }
  body {
    background: var(--page-bg);
    font-family: "Roboto", Arial, sans-serif;
    position: relative;
  }
  .card {
    position: absolute;
    left: 60px;
    top: 178px;
    width: 1080px;
    height: 615px;
    border-radius: 22px;
    overflow: hidden;
    box-shadow: 0 18px 40px rgba(0,0,0,0.25);
  }
  .card-bg { position: absolute; inset: 0; width: 100%; height: 100%; }
  .name-marker {
    position: absolute;
    left: -26px;
    top: 124px;
    width: 52px;
    height: 52px;
    border-radius: 50%;
    background: var(--accent-green);
  }
  .person-name {
    position: absolute;
    left: 53px;
    top: 120px;
    font-family: "Roboto Condensed", "Arial Narrow", sans-serif;
    font-weight: 700;
    font-size: 40px;
    color: var(--text-light);
    letter-spacing: 0.5px;
  }
  .person-title {
    position: absolute;
    left: 53px;
    top: 168px;
    font-size: 26px;
    color: var(--accent-green);
  }
  .address {
    position: absolute;
    left: 53px;
    top: 278px;
    font-size: 26px;
    line-height: 33px;
    color: var(--text-muted);
  }
  .contact-list {
    position: absolute;
    left: 53px;
    top: 370px;
    list-style: none;
  }
  .contact-item {
    display: flex;
    align-items: center;
    height: 40px;
    font-size: 26px;
    color: var(--text-muted);
  }
  .contact-icon { width: 26px; height: 22px; margin-right: 14px; flex: none; }
  .brand {
    position: absolute;
    left: 590px;
    top: 245px;
    width: 460px;
    display: flex;
    align-items: center;
    justify-content: center;
    gap: 18px;
  }
  .brand-square {
    width: 40px;
    height: 40px;
    background: var(--accent-green);
    flex: none;
  }
  .brand-name {
    font-family: "Roboto Condensed", "Arial Narrow", sans-serif;
    font-weight: 700;
    font-size: 44px;
    line-height: 48px;
    color: var(--brand-ink);
    text-transform: uppercase;
    letter-spacing: 1px;
  }
</style>
</head>
<body>
  <section class="card" aria-label="Business card">
    <svg class="card-bg" viewBox="0 0 1180 672" preserveAspectRatio="none" aria-hidden="true">
      <defs>
        <linearGradient id="frost" x1="0" y1="0" x2="1" y2="1">
          <stop offset="0" stop-color="var(--frost-mid)"/>
          <stop offset="0.5" stop-color="var(--frost-light)"/>
          <stop offset="1" stop-color="var(--frost-mid)"/>
        </linearGradient>
        <linearGradient id="dark" x1="0" y1="0" x2="1" y2="0">
          <stop offset="0" stop-color="var(--panel-dark-edge)"/>
          <stop offset="1" stop-color="var(--panel-dark)"/>
        </linearGradient>
      </defs>
      <rect width="1180" height="672" fill="url(#frost)"/>
      <path d="M0 0 H625 C560 120 530 250 545 380 C555 500 590 600 630 672 H0 Z" fill="url(#dark)"/>
      <path d="M632 0 C572 120 548 250 560 380 C570 500 602 600 638 672" fill="none" stroke="var(--accent-green)" stroke-width="5"/>
    </svg>

    <span class="name-marker" aria-hidden="true"></span>
    <h1 class="person-name">Mara Ellison</h1>
    <p class="person-title">Owner</p>

    <p class="address">PO BOX 480, Harbour Lane<br>7th street Ashford</p>

    <ul class="contact-list">
      <li class="contact-item">
        <svg class="contact-icon" viewBox="0 0 26 22" aria-hidden="true"><rect x="8" y="2" width="11" height="18" rx="1.5" fill="none" stroke="var(--accent-green)" stroke-width="2"/></svg>
        (555) 014-2273
      </li>
      <li class="contact-item">
        <svg class="contact-icon" viewBox="0 0 26 22" aria-hidden="true"><rect x="1" y="3" width="24" height="16" fill="var(--accent-green)"/><path d="M1 3 L13 12 L25 3 M1 19 L10 10 M25 19 L16 10" fill="none" stroke="var(--panel-dark)" stroke-width="1.6"/></svg>
        hello@summitlinebuild.com
      </li>
      <li class="contact-item">
        <svg class="contact-icon" viewBox="0 0 26 22" aria-hidden="true"><circle cx="13" cy="11" r="10" fill="none" stroke="var(--accent-green)" stroke-width="2"/><path d="M3 11 H23 M13 1 V21 M13 1 C7 6 7 16 13 21 M13 1 C19 6 19 16 13 21" fill="none" stroke="var(--accent-green)" stroke-width="1.4"/></svg>
        www.summitlinebuild.com
      </li>
    </ul>

    <div class="brand">
      <span class="brand-square" aria-hidden="true"></span>
      <p class="brand-name">Summitline<br>Design + Build</p>
    </div>
  </section>
</body>
</html>
```